Adult Literacy Program - flyer to attract volunteers and students

We want a flyer that is engaging, colorful, modern and will appeal to our primary audience of adults aged 40-60. We are trying to attract both prospective volunteers (typically age 50+, mostly women) and students (typically aged 40+).
The flyer should feature diverse people working together in pairs of two, reading or talking, with a workbook or some reading material in front of them.

Our organization trains tutors to work one-on-one with adults who are learning how to read. Most of our adult students are non-native speakers of English. Many are of Haitian or Hispanic origin, so we would like some people who represent that demographic.

The Flyer should represent reading, learning, literacy, knowledge, growth,
and opportunities.
Our students are learning to read so they can advance their job opportunities.

Target Market(s)

Adults aged 40-60, primarily women, retired, volunteers

Industry/Entity Type

Education

Font styles to use
Serif
Sans Serif

Colors

Designer to choose colors to be used in the design.

Requirements
Must have
• - UPDATE: Should be designed as a TRI-FOLD brochure on 8.5 x 11 inch paper that will be folded into thirds.
• - Images of diverse people, women and men, who look Hispanic, Haitian and other nationalities as well as Caucasian.
• - Our logo on the front cover
Nice to have
• The sample flyer is very boring and dry! We are open to different ways of presenting the text.

```html
<!DOCTYPE html>
<html lang="en">
<head>
<meta charset="utf-8">
<title>Pathways to Reading – Tri-fold Brochure</title>
<link href="https://fonts.googleapis.com/css2?family=PT+Sans:wght@400;700&family=Kaushan+Script&display=swap" rel="stylesheet">
<style>
  :root {
    --navy: #0b2f56;
    --cyan: #1ba6de;
    --white: #ffffff;
    --paper: #f3f3f4;
    --text: #4d4d4f;
    --stage: #d5d6d8;
    --photo-warm-a: #c9a27c;
    --photo-warm-b: #6f5a48;
  }
  * { margin: 0; padding: 0; box-sizing: border-box; }
  html, body { width: 815px; height: 1200px; overflow: hidden; }
  body { background: var(--stage); font-family: "PT Sans", Arial, sans-serif; color: var(--text); position: relative; }

  .sheet { position: absolute; left: 96px; width: 634px; height: 492px; }
  .sheet--outside { top: 54px; }
  .sheet--inside { top: 624px; }
  .sheet__art { position: absolute; inset: 0; width: 634px; height: 492px; }

  .abs { position: absolute; }
  .tab { position: absolute; height: 25px; background: var(--cyan); color: var(--white);
         font-weight: 700; font-size: 16px; line-height: 25px; padding-left: 14px; border-radius: 0 13px 13px 0; }
  .pill { position: absolute; color: var(--white); font-size: 11px; text-align: center; border-radius: 12px; }

  .body-copy { font-size: 9.6px; line-height: 16.6px; text-align: justify; color: var(--text); }
  .script { font-family: "Kaushan Script", cursive; }
  .center { text-align: center; }
  .caps-cta { font-size: 9px; color: var(--cyan); letter-spacing: 0.2px; }
  .phone { font-size: 10px; display: flex; align-items: center; justify-content: center; gap: 5px; }
  .phone svg { width: 10px; height: 10px; }
  .program-name { font-weight: 700; font-size: 15px; letter-spacing: 0.3px; }

  .bullets { list-style: none; font-size: 9.6px; line-height: 16.6px; color: var(--white); }
  .bullets li::before { content: "• "; }
  .bullets .sub { padding-left: 26px; }
  .bullets .cont { padding-left: 8px; }
  .bullets .cont::before { content: ""; }
</style>
</head>
<body>

<!-- Outside of the brochure -->
<section class="sheet sheet--outside">
  <svg class="sheet__art" viewBox="0 0 634 492" aria-hidden="false">
    <defs>
      <linearGradient id="paperShade" x1="0" x2="1"><stop offset="0" stop-color="#ffffff"/><stop offset="1" stop-color="#e4e5e7"/></linearGradient>
      <linearGradient id="photoWarm" x1="0" y1="0" x2="1" y2="1"><stop offset="0" stop-color="#8a7a6c"/><stop offset="1" stop-color="#d9c3a6"/></linearGradient>
      <linearGradient id="photoLibrary" x1="0" y1="0" x2="1" y2="1"><stop offset="0" stop-color="#b79a78"/><stop offset="1" stop-color="#e6d8c6"/></linearGradient>
      <linearGradient id="photoDesk" x1="0" y1="0" x2="0" y2="1"><stop offset="0" stop-color="#b9c8d6"/><stop offset="1" stop-color="#4c7fa8"/></linearGradient>
    </defs>
    <!-- panel: about -->
    <rect x="0" y="0" width="211" height="492" fill="url(#paperShade)"/>
    <path role="img" aria-label="Photo: an older man and a woman reading a book together at a library table" d="M0 352 Q105 318 211 336 V492 H0Z" fill="url(#photoWarm)"/>
    <path d="M0 330 Q105 290 211 310 V336 Q105 318 0 352Z" fill="var(--navy)"/>
    <path d="M0 352 Q105 318 211 336" stroke="var(--white)" stroke-width="3" fill="none"/>
    <!-- panel: contact -->
    <rect x="211" y="0" width="212" height="492" fill="var(--navy)"/>
    <path d="M211 340 Q320 372 423 384 V492 H211Z" fill="var(--cyan)"/>
    <circle cx="308" cy="322" r="55" fill="var(--white)"/>
    <circle role="img" aria-label="Photo: a smiling woman talking on the phone at a desk" cx="308" cy="322" r="51" fill="url(#photoDesk)"/>
    <!-- panel: cover -->
    <rect x="423" y="0" width="211" height="492" fill="var(--white)"/>
    <path role="img" aria-label="Photo: a smiling man with glasses holding a book in a library" d="M423 150 Q540 142 634 100 V420 H423Z" fill="url(#photoLibrary)"/>
    <path d="M423 140 Q545 132 634 88 V104 Q545 146 423 154Z" fill="var(--navy)"/>
    <path d="M423 154 Q545 146 634 104" stroke="var(--cyan)" stroke-width="4" fill="none"/>
    <path d="M423 392 Q545 392 634 350 V492 H423Z" fill="var(--cyan)"/>
    <path d="M423 392 Q545 392 634 350" stroke="var(--white)" stroke-width="3" fill="none"/>
  </svg>

  <!-- about panel -->
  <div class="tab" style="left:0; top:29px; width:121px;">About Us</div>
  <p class="abs body-copy" style="left:12px; top:86px; width:188px;">We are recruiting volunteers who can tutor at the Maple Branch, Cedar Grove Branch, Riverside Branch, Harbor View Branch (Eastport), Main Library (Central Avenue) and the Lakeside Boulevard Branch. Registration is required to participate. Tutors must attend all sessions to volunteer with our program.</p>
  <p class="abs body-copy" style="left:12px; top:230px; width:188px;">Workshops are based on student demand. Please call the Volunteer Desk at 555-014-2200 for more information.</p>

  <!-- contact panel -->
  <div class="abs center" style="left:211px; top:104px; width:212px;">
    <span class="program-name" style="color:var(--white);">Pathways to Reading</span>
  </div>
  <p class="abs center script" style="left:211px; top:162px; width:212px; font-size:15px; color:var(--white);">Don't waste a moment!</p>
  <p class="abs center caps-cta" style="left:211px; top:189px; width:212px;">CONTACT US TODAY TO LEARN MORE.</p>
  <div class="abs phone" style="left:211px; top:206px; width:212px; color:var(--white);">
    <svg viewBox="0 0 10 10"><circle cx="5" cy="5" r="4.4" fill="none" stroke="currentColor" stroke-width="0.9"/><path d="M3.4 2.8 l0.9 -0.3 0.5 1.1 -0.6 0.5 q0.4 0.9 1.3 1.4 l0.5 -0.6 1.1 0.5 -0.3 0.9 q-2.9 0 -3.4 -3.5z" fill="currentColor"/></svg>
    <span>555-014-2200</span>
  </div>
  <div class="pill" style="left:252px; top:399px; width:114px; height:19px; line-height:19px; background:var(--navy);">CONTACT US</div>
  <p class="abs center" style="left:211px; top:424px; width:212px; font-size:8.8px; line-height:15.3px; color:var(--white);">Volunteer Desk: 555-014-2200<br>Cedar Grove, Eastport &amp; Lakeside:<br>555-014-7300<br>email: literacy@examplelibrary.org</p>

  <!-- cover panel -->
  <div class="abs center" style="left:423px; top:88px; width:211px;">
    <span class="program-name" style="color:var(--navy);">Pathways to Reading</span>
  </div>
  <p class="abs center" style="left:423px; top:414px; width:211px; font-size:17.5px; color:var(--white); letter-spacing:0.4px;">VOLUNTEER</p>
  <p class="abs center" style="left:433px; top:443px; width:191px; font-size:12px; line-height:16.5px; color:var(--white);">Help an adult learn to read, write or speak English</p>
</section>

<!-- Inside of the brochure -->
<section class="sheet sheet--inside">
  <svg class="sheet__art" viewBox="0 0 634 492">
    <defs>
      <linearGradient id="photoPair" x1="0" y1="0" x2="1" y2="1"><stop offset="0" stop-color="#d8c2a2"/><stop offset="1" stop-color="#9c6b5c"/></linearGradient>
      <linearGradient id="photoGroup" x1="0" y1="0" x2="1" y2="0"><stop offset="0" stop-color="#c4b18d"/><stop offset="1" stop-color="#7c6a55"/></linearGradient>
      <linearGradient id="photoLaptop" x1="0" y1="0" x2="1" y2="1"><stop offset="0" stop-color="#b7a58d"/><stop offset="1" stop-color="#e4ddd2"/></linearGradient>
      <linearGradient id="paperShadeInside" x1="0" x2="1"><stop offset="0" stop-color="#ffffff"/><stop offset="1" stop-color="#ececee"/></linearGradient>
    </defs>
    <!-- panel: tutors -->
    <rect x="0" y="0" width="211" height="492" fill="var(--navy)"/>
    <path role="img" aria-label="Photo: a volunteer tutor and an adult student reading a workbook together" d="M0 0 H211 V196 Q110 196 0 222Z" fill="url(#photoPair)"/>
    <path d="M0 222 Q110 196 211 196 V212 Q110 206 0 236Z" fill="var(--white)"/>
    <path d="M0 222 Q110 196 211 196" stroke="var(--cyan)" stroke-width="5" fill="none"/>
    <!-- panel: volunteer -->
    <rect x="211" y="0" width="212" height="492" fill="url(#paperShadeInside)"/>
    <rect role="img" aria-label="Photo: a diverse group of adults studying together at a library table" x="211" y="242" width="212" height="140" fill="url(#photoGroup)"/>
    <!-- panel: students -->
    <rect x="423" y="0" width="211" height="492" fill="var(--navy)"/>
    <path role="img" aria-label="Photo: a woman and a man talking over a laptop in a library" d="M423 330 Q540 320 634 282 V492 H423Z" fill="url(#photoLaptop)"/>
    <path d="M423 316 Q540 318 634 270 V282 Q540 320 423 330Z" fill="var(--white)"/>
    <path d="M423 330 Q540 320 634 282" stroke="var(--cyan)" stroke-width="4" fill="none"/>
  </svg>

  <!-- tutors panel -->
  <div class="tab" style="left:0; top:246px; width:121px;">TUTORS</div>
  <ul class="abs bullets" style="left:14px; top:289px; width:192px;">
    <li>No special skills or degrees needed</li>
    <li class="cont">just a degree of caring!</li>
    <li>Training offered throughout the year</li>
    <li>Tutors meet students weekly at a library</li>
    <li>Instructional materials provided</li>
    <li>Ongoing support available</li>
  </ul>
  <p class="abs center script" style="left:0; top:417px; width:211px; font-size:12px; line-height:18px; color:var(--white);">Teach an adult to read<br>and you'll change a<br>life forever.</p>

  <!-- volunteer panel -->
  <p class="abs center script" style="left:211px; top:44px; width:212px; font-size:25px; color:var(--cyan);">Enrich a Life!</p>
  <div class="pill" style="left:270px; top:95px; width:142px; height:24px; line-height:24px; background:var(--cyan); font-size:16px; font-weight:700; letter-spacing:0.5px;">VOLUNTEER</div>
  <p class="abs center" style="left:213px; top:138px; width:208px; font-size:9.6px; line-height:16.6px; color:var(--text);">Volunteer a few hours each week and<br>make a difference.<br>Teach an adult to read, write or speak English.<br>Materials and training are offered<br>free-of-charge.</p>
  <p class="abs center script" style="left:211px; top:412px; width:212px; font-size:13px; color:var(--navy);">Don't waste a moment!</p>
  <p class="abs center caps-cta" style="left:211px; top:436px; width:212px;">CONTACT US TODAY TO LEARN MORE.</p>
  <div class="abs phone" style="left:211px; top:453px; width:212px; color:var(--navy);">
    <svg viewBox="0 0 10 10"><circle cx="5" cy="5" r="4.4" fill="none" stroke="currentColor" stroke-width="0.9"/><path d="M3.4 2.8 l0.9 -0.3 0.5 1.1 -0.6 0.5 q0.4 0.9 1.3 1.4 l0.5 -0.6 1.1 0.5 -0.3 0.9 q-2.9 0 -3.4 -3.5z" fill="currentColor"/></svg>
    <span>555-014-2200</span>
  </div>

  <!-- students panel -->
  <div class="tab" style="left:423px; top:33px; width:118px;">STUDENTS</div>
  <ul class="abs bullets" style="left:436px; top:78px; width:196px;">
    <li>Students are adults in need of</li>
    <li class="sub">basic literacy skills</li>
    <li class="sub">pre-GED skills</li>
    <li class="sub">conversational English</li>
    <li>Tutoring is free of charge</li>
    <li>Tutoring is one-on-one</li>
    <li>Flexible scheduling during library hours</li>
    <li>Lessons focus on student goals</li>
  </ul>
  <p class="abs center script" style="left:423px; top:222px; width:211px; font-size:12px; line-height:18px; color:var(--white);">If you can read,<br>you can tutor!</p>
</section>

</body>
</html>
```